Bright, Bold Sydney Tutoring Business Flyer Advertisment

Lumivora is an up and coming tutoring business located on Sydney's Upper North Shore catering to school students of all ages. We need a flyer designed for notice boards and letter box drops to attract new clients. Our tutors are mostly university education students who are fresh, dedicated and passionate about their areas of teaching. The flyer should exhibit a bright, bold, modern, clean cut style which would appeal to both students and parents. I have attached our logo (the flyer could reflect this colour scheme), and a PDF which outlines the information we would like to appear on the flyer. This is not set in stone, but designed to act as an extremely loose guide for your creativity !

Target Market(s)

Affluent School Students and Parents

Industry/Entity Type

Tutoring

Requirements
Must have
• Logo, $10 offer, company description.
Nice to have
• Grabbing headlines to attract new clients, such as "Feeling overwhelmed at school?". We are looking for an eye catching, clean cut and professional design that has the colours to attract kids and the tone to attract parents.

```html
<!DOCTYPE html>
<html lang="en">
<head>
<meta charset="UTF-8">
<title>Lumivora Tutoring Flyer</title>
<link rel="stylesheet" href="https://fonts.googleapis.com/css2?family=Roboto+Condensed:wght@400;700;900&display=swap">
<style>
  :root {
    --ink: #111111;
    --grey: #4a4a4a;
    --pink: #f7b6da;
    --pink-soft: #fbe3f1;
    --sky: #85d4f1;
    --sky-soft: #e8f5fb;
    --white: #ffffff;
  }
  * { margin: 0; padding: 0; box-sizing: border-box; }
  html, body { width: 862px; height: 1200px; overflow: hidden; background: var(--white); }
  body { font-family: "Roboto Condensed", "Arial Narrow", sans-serif; color: var(--ink); }

  .flyer {
    position: relative;
    width: 862px;
    height: 1200px;
    overflow: hidden;
    background: linear-gradient(160deg, var(--pink-soft) 0%, #fdf3f9 18%, var(--white) 40%, var(--sky-soft) 60%, var(--white) 72%);
  }

  .accent-bar {
    position: absolute;
    background: var(--pink);
  }
  .accent-bar--headline { left: 19px; top: 106px; width: 40px; height: 92px; }
  .accent-bar--offer { left: 812px; top: 990px; width: 38px; height: 136px; }

  .headline {
    position: absolute;
    left: 77px;
    top: 100px;
    font-weight: 900;
    font-size: 47px;
    line-height: 1.02;
    text-transform: uppercase;
    letter-spacing: 0.2px;
  }

  .question {
    position: absolute;
    left: 77px;
    font-weight: 900;
    font-size: 27px;
    line-height: 1.1;
    text-transform: uppercase;
  }
  .question--hsc { top: 310px; }
  .question--engagement { top: 440px; }

  .hero-photo {
    position: absolute;
    left: 345px;
    top: 285px;
    width: 470px;
    height: 392px;
    background:
      radial-gradient(ellipse at 55% 40%, #cfe9f5 0%, #e4f3fa 45%, rgba(255,255,255,0) 75%),
      linear-gradient(180deg, rgba(255,255,255,0) 70%, #f4f4f4 100%);
  }

  .info-band {
    position: absolute;
    left: 0;
    top: 676px;
    width: 862px;
    height: 204px;
    background: var(--sky);
  }
  .info-band__dividers { position: absolute; inset: 0; }
  .info-band__text {
    position: absolute;
    top: 30px;
    color: var(--white);
    font-size: 21px;
    line-height: 1.12;
  }
  .info-band__text strong { font-weight: 700; }
  .info-band__text--service { left: 96px; width: 320px; }
  .info-band__text--tutors { left: 468px; width: 350px; }

  .brand {
    position: absolute;
    left: 50px;
    top: 930px;
    width: 140px;
    text-align: center;
  }
  .brand__mark {
    display: block;
    width: 110px;
    height: 110px;
    margin: 0 auto 12px;
    border-radius: 50%;
    background: var(--sky);
  }
  .brand__name {
    font-size: 32px;
    font-weight: 700;
    color: var(--grey);
  }

  .contact {
    position: absolute;
    left: 212px;
    top: 926px;
    width: 240px;
    font-size: 15.5px;
    line-height: 1.22;
    color: var(--grey);
  }
  .contact strong { color: var(--ink); font-weight: 700; }
  .contact__lead { margin-bottom: 16px; }

  .offer {
    position: absolute;
    right: 62px;
    top: 992px;
    text-align: right;
    font-weight: 900;
    text-transform: uppercase;
  }
  .offer__lead { font-size: 22px; line-height: 1.05; }
  .offer__price { font-size: 62px; line-height: 1; margin-top: 2px; }
</style>
</head>
<body>
<main class="flyer">
  <div class="accent-bar accent-bar--headline"></div>
  <h1 class="headline">Looking to improve<br>your skills, confidence<br>and organization?</h1>

  <h2 class="question question--hsc">Feeling<br>overwhelmed<br>by the HSC?</h2>
  <h2 class="question question--engagement">Want to<br>increase<br>your child’s<br>engagement<br>at school?</h2>

  <div class="hero-photo" role="img" aria-label="Photo of a smiling young student in glasses leaning on an open book"></div>

  <section class="info-band">
    <svg class="info-band__dividers" width="862" height="204" viewBox="0 0 862 204" aria-hidden="true">
      <line x1="92" y1="0" x2="76" y2="170" stroke="#ffffff" stroke-width="2"/>
      <line x1="452" y1="0" x2="436" y2="170" stroke="#ffffff" stroke-width="2"/>
    </svg>
    <p class="info-band__text info-band__text--service">Lumivora <strong>Tutoring</strong> offers <strong>one-on-one, individualized learning</strong> experiences to maximize academic <strong>development</strong>.</p>
    <p class="info-band__text info-band__text--tutors">Our <strong>tutors</strong> are hand selected on the basis of their qualifications, <strong>expertise</strong> and <strong>passion</strong> for inspiring young learners.</p>
  </section>

  <div class="brand">
    <span class="brand__mark"></span>
    <span class="brand__name">Lumivora</span>
  </div>

  <div class="contact">
    <p class="contact__lead"><strong>Contact us</strong> today to discuss how we can help make your learning goals a reality!</p>
    <p>info@lumivoratutoring.com.au<br>www.lumivoratutoring.com.au<br>Suite 4, 218<br>Wattle Grove Road Turramurra,<br>NSW 2074</p>
  </div>

  <div class="offer">
    <p class="offer__lead">Mention this<br>advertisement to<br>claim your trial<br>session for just</p>
    <p class="offer__price">$10!</p>
  </div>
  <div class="accent-bar accent-bar--offer"></div>
</main>
</body>
</html>
```